PREMIUM AGENCY High End Business Card - A+++ Designers Wanted

** DO NOT ATTEMPT TO CONTACT ME THROUGH SEARCHING ON ZINTREL OR EMAILING ME THROUGH MY WEBSITE **

I need a fresh, contemporary business card designed using the logo attached (BRONSALK)

I have attached the font for BRONSALK

It must have a premium look and feel. The business card size must be STANDARD size.

You can submit either/both VERTICAL or HORIZONTAL designs.

FRONT: It must have the following sample information on

Paul Ardley
Director Operations
Mobile +61 452 118 906
Email paulardley@bronsalk.com
www.bronsalk.com

The REAR of the business card must have the words

CREATE INSPIRE TOMORROW

as part of the design, in the same font (NEXA) attached.

The words do not need to be in capitals, or on the same line, please design this as you see it best working.

ADDITIONAL INFORMATION
======================

The BRONSALK logo must be on the front of the card

I want Ultraviolet printing on the final design, to enhance either the NAME of the person OR the BRONSALK logo OR the words on the back of the card.

Target Market(s)

Agency, Advertising Agency, Creative, Designers

Industry/Entity Type

Media

Contact Information for Business Card

Design Agency, Contemporary, Premium look and feel, High Quality

Font styles to use
Serif
Sans Serif
Other font styles liked:
• ATTACHED TO PROJECT

Requirements
Must have
• BLACK & WHITE as the primary design, and if you feel there can be a highlighted colour, then this can be used.
• The Logo ICON attached is blue, this colour must not be changed.
• I have attached the partner brand BRONSALK MEDIA incase you need to manipulate the original files.
• ** DO NOT ATTEMPT TO CONTACT ME THROUGH SEARCHING ON ZINTREL OR EMAILING ME THROUGH MY WEBSITE **
Nice to have
• Must be Premium. I have attached some sample designs, that I like that would be a good inspiration for where this can be taken.
• My favourite design is is the KESTRAVUE2-BUSINESSCARD-TEMPLATE
Should not have
• No funny or silly standard / off the shelf designs

```html
<!DOCTYPE html>
<html lang="en">
<head>
<meta charset="utf-8">
<title>Bronsalk Business Card</title>
<link rel="stylesheet" href="https://fonts.googleapis.com/css2?family=Montserrat:wght@400;500;600;700&display=swap">
<style>
  :root {
    --stage: #e9e5df;
    --card: #434447;
    --card-edge: #2c2d30;
    --ink-dark: #1d1d1f;
    --brand-blue: #27a6e0;
    --steel-blue: #5a8fa9;
    --paper-white: #f4f6f7;
    --rule: rgba(255,255,255,0.55);
  }
  * { box-sizing: border-box; margin: 0; padding: 0; }
  html, body {
    width: 1200px; height: 1023px; overflow: hidden;
    background: var(--stage);
    font-family: "Montserrat", sans-serif;
  }
  .stage { position: relative; width: 1200px; height: 1023px; }

  .card {
    position: absolute;
    background: var(--card);
    box-shadow: 0 6px 0 var(--card-edge), 0 18px 30px rgba(0,0,0,0.25);
    overflow: hidden;
  }
  .card-bands { position: absolute; inset: 0; }

  /* Rear card (horizontal) */
  .card-rear { left: 70px; top: 150px; width: 600px; height: 340px; }
  .rear-brand {
    position: absolute; left: 0; right: 0; top: 100px;
    display: flex; align-items: center; justify-content: center; gap: 22px;
  }
  .brand-dot {
    width: 34px; height: 34px; border-radius: 50%;
    background: var(--brand-blue); flex: none;
  }
  .brand-name {
    color: var(--ink-dark); font-weight: 600; letter-spacing: 0.12em;
    line-height: 1;
  }
  .rear-brand .brand-name { font-size: 62px; }
  .tagline {
    position: absolute; left: 30px; width: 410px; bottom: 22px;
    display: flex; align-items: center; gap: 14px;
    color: var(--paper-white); font-size: 21px; font-weight: 400;
    white-space: nowrap;
  }
  .tagline::before, .tagline::after {
    content: ""; flex: 1; height: 1px; background: var(--paper-white);
  }

  /* Front card (vertical) */
  .card-front { left: 770px; top: 250px; width: 340px; height: 600px; }
  .front-brand {
    position: absolute; left: 22px; top: 360px;
    display: flex; align-items: center; gap: 16px;
    transform: rotate(-90deg); transform-origin: left top;
  }
  .front-brand .brand-name { font-size: 34px; }
  .front-brand .brand-dot { width: 24px; height: 24px; order: -1; }

  .person { position: absolute; right: 28px; top: 38px; text-align: right; }
  .person-name {
    color: var(--brand-blue); font-weight: 700; line-height: 0.88;
  }
  .person-first { display: block; font-size: 60px; }
  .person-last { display: block; font-size: 44px; }
  .person-role {
    display: inline-block; margin-top: 8px; padding-right: 10px;
    border-right: 1px solid var(--paper-white);
    color: var(--paper-white); font-size: 14px; line-height: 1.15;
  }

  .contacts { position: absolute; left: 26px; right: 26px; top: 352px; list-style: none; }
  .contact {
    display: flex; align-items: center; gap: 14px;
    height: 40px; border-bottom: 1px solid var(--rule);
    color: var(--paper-white); font-size: 19px; font-weight: 600;
  }
  .contact:last-child { border-bottom: none; }
  .contact svg { width: 18px; height: 18px; flex: none; }
</style>
</head>
<body>
<main class="stage">

  <section class="card card-rear" aria-label="Card back">
    <svg class="card-bands" viewBox="0 0 600 340" preserveAspectRatio="none" aria-hidden="true">
      <polygon points="460,236 600,236 600,340 520,340" fill="var(--steel-blue)"/>
      <polygon points="0,276 450,276 480,248 540,248 500,340 0,340" fill="var(--brand-blue)"/>
    </svg>
    <div class="rear-brand">
      <span class="brand-dot"></span>
      <span class="brand-name">BRONSALK</span>
    </div>
    <p class="tagline">Create inspire tomorrow</p>
  </section>

  <section class="card card-front" aria-label="Card front">
    <svg class="card-bands" viewBox="0 0 340 600" preserveAspectRatio="none" aria-hidden="true">
      <polygon points="0,548 340,548 340,600 0,600" fill="var(--steel-blue)"/>
      <polygon points="40,530 340,500 340,560 30,560" fill="var(--brand-blue)"/>
    </svg>

    <div class="front-brand">
      <span class="brand-dot"></span>
      <span class="brand-name">BRONSALK</span>
    </div>

    <header class="person">
      <h1 class="person-name">
        <span class="person-first">Paul</span>
        <span class="person-last">Ardley</span>
      </h1>
      <p class="person-role">Director<br>Operations</p>
    </header>

    <ul class="contacts">
      <li class="contact">
        <svg viewBox="0 0 18 18" aria-hidden="true"><rect x="5" y="1" width="8" height="16" rx="1.5" fill="none" stroke="#f4f6f7" stroke-width="1.6"/><line x1="7.5" y1="14" x2="10.5" y2="14" stroke="#f4f6f7" stroke-width="1.4"/></svg>
        <span>+61 452 118 906</span>
      </li>
      <li class="contact">
        <svg viewBox="0 0 18 18" aria-hidden="true"><rect x="1" y="4" width="16" height="11" fill="#f4f6f7"/><polyline points="1,4 9,10 17,4" fill="none" stroke="#434447" stroke-width="1.4"/></svg>
        <span>paulardley@bronsalk.com</span>
      </li>
      <li class="contact">
        <svg viewBox="0 0 18 18" aria-hidden="true"><circle cx="9" cy="9" r="7.5" fill="none" stroke="#f4f6f7" stroke-width="1.3"/><ellipse cx="9" cy="9" rx="3.2" ry="7.5" fill="none" stroke="#f4f6f7" stroke-width="1.1"/><line x1="1.5" y1="9" x2="16.5" y2="9" stroke="#f4f6f7" stroke-width="1.1"/></svg>
        <span>www.bronsalk.com</span>
      </li>
    </ul>
  </section>

</main>
</body>
</html>
```